Flash Banners for CampusLantern.com

We are running a media campaign to drive traffic to CampusLantern.com. Campus Lantern allows people that are interested in pursuing an advanced degree to find colleges and universities that offer their program and level of study.

We would like to have Flash Interactive banners created that grab people’s attention and have a high click-thru rate for our CPM Media Campaign.

BANNER MESSAGING/CLICKABLE ELEMENTS:
Headline: Earn Your Degree Online!

Clickable Elements with Rollover Animation and/or Icons:
GROUPING 1
Nursing
Education
Legal
Design
And more
GROUPING 2
Associates
Bachelor’s
Master’s
Doctorate
(Each group should have some kind of visual separation, no need to label
Group1 or Group 2)

Call To Action: Find Schools

Logo: CampusLantern

• We would like animated flash banners in the following sizes:
300x250
728x90
160x600

The spec requirements are:
24 FPS (Frames per second)
30 seconds max animation, looping back to beginning
120K Max File Size
Final .swf file & Original .FLA file with layers

```html
<!DOCTYPE html>
<html lang="en">
<head>
<meta charset="utf-8">
<title>CampusLantern – Flash Animation Storyboard</title>
<link rel="stylesheet" href="https://fonts.googleapis.com/css2?family=Source+Sans+3:wght@400;600;700&display=swap">
<style>
  :root{
    --stage:#000000;
    --title:#ffffff;
    --chalk-light:#5a8a68;
    --chalk-dark:#34563f;
    --strip:#ffffff;
    --brand:#1f4a5a;
    --brand-accent:#e8581c;
    --cta-top:#5b86a4;
    --cta-bottom:#3d6886;
    --bezel:#111214;
    --bezel-edge:#3a3b3e;
    --base-light:#e9eaec;
    --base-dark:#a8abb0;
    --nursing:#c0301a;
    --nursing-dark:#7a1a0c;
    --business:#c8c8c8;
    --business-dark:#8d8d8d;
    --education:#7fb06e;
    --education-dark:#4f8245;
    --legal:#5f9cb0;
    --legal-dark:#3a6f82;
    --design:#c4257e;
    --design-dark:#7f1450;
    --more:#7a4a98;
    --more-dark:#4f2a6a;
    --label:#ffffff;
  }
  *{box-sizing:border-box;margin:0;padding:0}
  html,body{width:1200px;height:900px;overflow:hidden;background:var(--stage)}
  body{position:relative;font-family:"Source Sans 3",Arial,sans-serif}
  .storyboard-title{
    position:absolute;top:16px;left:0;width:1200px;text-align:center;
    color:var(--title);font-weight:700;font-size:20px;letter-spacing:.2px;word-spacing:4px
  }
  .frame{position:absolute;width:300px;height:250px;background:var(--strip);overflow:hidden}
  .art{position:absolute;left:0;top:0;width:300px;height:200px}
  .art--chalk{background:radial-gradient(ellipse at 50% 40%,var(--chalk-light),var(--chalk-dark))}
  .art--studio{background:linear-gradient(#ffffff,#f1f2f3)}
  .bezel{
    position:absolute;left:13px;top:6px;width:274px;height:182px;
    background:var(--bezel);border:1px solid var(--bezel-edge);border-radius:8px 8px 0 0
  }
  .screen{
    position:absolute;left:10px;top:12px;width:252px;height:158px;overflow:hidden;
    display:flex;flex-direction:column;align-items:center;justify-content:flex-end;padding-bottom:20px
  }
  .base{
    position:absolute;left:0;top:187px;width:300px;height:13px;
    background:linear-gradient(var(--base-light),var(--base-dark));
    border-radius:0 0 6px 6px
  }
  .screen--nursing{background:radial-gradient(circle at 50% 45%,var(--nursing),var(--nursing-dark))}
  .screen--business{background:radial-gradient(circle at 50% 45%,var(--business),var(--business-dark))}
  .screen--education{background:radial-gradient(circle at 50% 45%,var(--education),var(--education-dark))}
  .screen--legal{background:radial-gradient(circle at 50% 45%,var(--legal),var(--legal-dark))}
  .screen--design{background:radial-gradient(circle at 50% 45%,var(--design),var(--design-dark))}
  .screen--more{background:radial-gradient(circle at 50% 50%,var(--more),var(--more-dark));justify-content:center;padding-bottom:0}
  .screen--transition{background:linear-gradient(90deg,var(--nursing) 0%,#e0442a 40%,#bdbdbd 55%,#9a9a9a 100%)}
  .icon{width:90px;height:60px;margin-bottom:8px;border-radius:8px;opacity:.85}
  .icon--cross{width:48px;height:48px;background:#f1f1f1;clip-path:polygon(33% 0,67% 0,67% 33%,100% 33%,100% 67%,67% 67%,67% 100%,33% 100%,33% 67%,0 67%,0 33%,33% 33%)}
  .icon--briefcase{background:linear-gradient(#3b3b3b,#141414)}
  .icon--book{width:40px;height:62px;background:linear-gradient(90deg,#4a5a66,#9fb3c0)}
  .icon--gavel{width:130px;height:42px;background:linear-gradient(90deg,#a8612e,#5e2e12);border-radius:20px}
  .icon--brush{width:110px;height:46px;background:linear-gradient(90deg,#c26a2a,#7a3a14);border-radius:20px}
  .label{color:var(--label);font-weight:700;font-size:35px;line-height:1;letter-spacing:-.5px;text-shadow:0 2px 4px rgba(0,0,0,.45)}
  .headline{
    position:absolute;left:0;width:300px;text-align:center;color:var(--label);
    font-weight:700;font-size:29px;line-height:32px;letter-spacing:-.3px;text-shadow:0 2px 4px rgba(0,0,0,.4)
  }
  .mini-laptop{position:absolute;left:80px;top:88px;width:140px;height:96px}
  .mini-laptop .bezel{left:4px;top:0;width:132px;height:88px;border-radius:5px 5px 0 0}
  .mini-laptop .screen{left:5px;top:6px;width:120px;height:76px;background:#ffffff;padding:0}
  .mini-laptop .base{left:-4px;top:87px;width:148px;height:7px}
  .strip{position:absolute;left:0;top:200px;width:300px;height:50px;background:var(--strip)}
  .brand{
    position:absolute;left:12px;top:15px;display:flex;align-items:center;gap:6px;
    color:var(--brand);font-weight:600;font-size:19px;letter-spacing:-.2px;line-height:1
  }
  .brand-mark{width:13px;height:13px;background:var(--brand-accent)}
  .cta{
    position:absolute;left:176px;top:10px;width:115px;height:32px;border-radius:3px;
    background:linear-gradient(var(--cta-top),var(--cta-bottom));
    color:#ffffff;font-weight:600;font-size:17px;line-height:32px;text-align:center;text-decoration:none
  }
</style>
</head>
<body>
  <h1 class="storyboard-title">FLASH ANIMATION STORYBOARD</h1>

  <article class="frame" style="left:118px;top:62px">
    <div class="art art--chalk"><p class="headline" style="top:70px">Earn your<br>degree online!</p></div>
    <footer class="strip"><span class="brand"><span class="brand-mark"></span>campuslantern</span><a class="cta" href="#">Find Schools</a></footer>
  </article>

  <article class="frame" style="left:438px;top:62px">
    <div class="art art--studio">
      <div class="bezel"><div class="screen screen--nursing"><div class="icon icon--cross"></div><p class="label">Nursing</p></div></div>
      <div class="base"></div>
    </div>
    <footer class="strip"><span class="brand"><span class="brand-mark"></span>campuslantern</span><a class="cta" href="#">Find Schools</a></footer>
  </article>

  <article class="frame" style="left:758px;top:62px">
    <div class="art art--chalk">
      <div class="bezel"><div class="screen screen--transition" role="img" aria-label="Motion-blurred transition from the Nursing screen to the Business screen"></div></div>
      <div class="base"></div>
    </div>
    <footer class="strip"><span class="brand"><span class="brand-mark"></span>campuslantern</span><a class="cta" href="#">Find Schools</a></footer>
  </article>

  <article class="frame" style="left:118px;top:343px">
    <div class="art art--studio">
      <div class="bezel"><div class="screen screen--business"><div class="icon icon--briefcase" role="img" aria-label="Black leather briefcase"></div><p class="label">Business</p></div></div>
      <div class="base"></div>
    </div>
    <footer class="strip"><span class="brand"><span class="brand-mark"></span>campuslantern</span><a class="cta" href="#">Find Schools</a></footer>
  </article>

  <article class="frame" style="left:438px;top:343px">
    <div class="art art--studio">
      <div class="bezel"><div class="screen screen--education"><div class="icon icon--book" role="img" aria-label="Standing hardcover book"></div><p class="label">Education</p></div></div>
      <div class="base"></div>
    </div>
    <footer class="strip"><span class="brand"><span class="brand-mark"></span>campuslantern</span><a class="cta" href="#">Find Schools</a></footer>
  </article>

  <article class="frame" style="left:758px;top:343px">
    <div class="art art--studio">
      <div class="bezel"><div class="screen screen--legal"><div class="icon icon--gavel" role="img" aria-label="Wooden judge's gavel on its block"></div><p class="label">Legal</p></div></div>
      <div class="base"></div>
    </div>
    <footer class="strip"><span class="brand"><span class="brand-mark"></span>campuslantern</span><a class="cta" href="#">Find Schools</a></footer>
  </article>

  <article class="frame" style="left:118px;top:622px">
    <div class="art art--studio">
      <div class="bezel"><div class="screen screen--design"><div class="icon icon--brush" role="img" aria-label="Wooden paintbrush"></div><p class="label">Design</p></div></div>
      <div class="base"></div>
    </div>
    <footer class="strip"><span class="brand"><span class="brand-mark"></span>campuslantern</span><a class="cta" href="#">Find Schools</a></footer>
  </article>

  <article class="frame" style="left:438px;top:622px">
    <div class="art art--studio">
      <div class="bezel"><div class="screen screen--more"><p class="label">&amp; more</p></div></div>
      <div class="base"></div>
    </div>
    <footer class="strip"><span class="brand"><span class="brand-mark"></span>campuslantern</span><a class="cta" href="#">Find Schools</a></footer>
  </article>

  <article class="frame" style="left:758px;top:622px">
    <div class="art art--chalk">
      <p class="headline" style="top:12px">Earn your<br>degree online!</p>
      <div class="mini-laptop">
        <div class="bezel"><div class="screen"></div></div>
        <div class="base"></div>
      </div>
    </div>
    <footer class="strip"><span class="brand"><span class="brand-mark"></span>campuslantern</span><a class="cta" href="#">Find Schools</a></footer>
  </article>
</body>
</html>
```